TRENDY & MODERN BUSINESS CARD DESIGN for Media Company *

I need a minimalistic - clean - modern and professional business card layout and design for MEDIA & PHOTOGRAPHY STUDIO.

We do NOT have a logo, and not really looking for one - but rather excellent typography and design. We would consider the 3 as a focal point.

We do personal and commercial photography.

Target Market(s)

Personal and commercial photography clientele

Contact Information for Business Card

ZUB size - from zub.com / size guidelines are enclosed in the brief

Font styles to use
Sans Serif

Colors
f78f20
eda3c7
cee9f5
0555a3
e667a6
fbf289

Requirements
Must have
• Clean lines - Modern layout
Nice to have
• All blue background as an option - use color palette in brief please.
Should not have
• Old fashion fonts and regular fonts.

```html
<!DOCTYPE html>
<html lang="en">
<head>
<meta charset="utf-8">
<title>Lumen North Media – Business Cards</title>
<link href="https://fonts.googleapis.com/css2?family=Barlow:ital,wght@0,400;0,500;0,600;1,400&family=Barlow+Semi+Condensed:wght@500;600&display=swap" rel="stylesheet">
<style>
  :root {
    --stage: #1b1b1b;
    --navy-light: #262878;
    --navy-dark: #14165a;
    --white: #ffffff;
    --pink: #eda3c7;
    --orange: #f78f20;
    --rule: rgba(206, 233, 245, 0.28);
  }
  * { box-sizing: border-box; margin: 0; padding: 0; }
  html, body { width: 1200px; height: 1200px; overflow: hidden; }
  body {
    background: var(--stage);
    font-family: "Barlow", Arial, sans-serif;
    color: var(--white);
    position: relative;
  }
  .card {
    position: absolute;
    top: 232px;
    width: 420px;
    height: 735px;
    background: radial-gradient(ellipse at 50% 45%, var(--navy-light) 0%, var(--navy-dark) 85%);
    box-shadow: 0 10px 30px rgba(0,0,0,0.55);
    overflow: hidden;
  }
  .card--info { left: 150px; }
  .card--brand { left: 630px; }

  .corners { position: absolute; inset: 0; width: 100%; height: 100%; }
  .corners path { fill: none; stroke: var(--white); stroke-width: 3; }

  .pattern-area {
    position: absolute; inset: 0;
    background: linear-gradient(160deg, rgba(60,64,150,0.35), rgba(20,22,90,0.1) 60%, rgba(60,64,150,0.3));
  }

  .brand { position: absolute; left: 0; right: 0; text-align: center; }
  .card--info .brand { top: 78px; }
  .card--brand .brand { top: 300px; }
  .brand__name {
    font-family: "Barlow Semi Condensed", "Arial Narrow", sans-serif;
    font-weight: 600;
    font-size: 40px;
    letter-spacing: 0.5px;
    line-height: 1;
    color: var(--white);
  }
  .brand__tagline {
    margin-top: 10px;
    font-size: 19px;
    letter-spacing: 1px;
    color: var(--pink);
  }

  .details { position: absolute; left: 56px; right: 40px; top: 300px; }
  .person__name {
    font-family: "Barlow Semi Condensed", "Arial Narrow", sans-serif;
    font-weight: 600; font-size: 34px; line-height: 1.05; letter-spacing: 0.5px;
  }
  .person__role {
    font-family: "Barlow Semi Condensed", "Arial Narrow", sans-serif;
    font-weight: 500; font-size: 21px; color: var(--pink); margin-top: 2px;
  }
  .rule { height: 1px; background: var(--rule); margin: 20px 0 18px; width: 88%; }
  .contact { list-style: none; }
  .contact li { display: flex; align-items: flex-start; gap: 12px; font-size: 19px; line-height: 1.3; margin-bottom: 6px; }
  .contact svg { flex: none; width: 26px; height: 26px; }
  .contact .icon-bg { fill: var(--pink); }
  .contact .icon-line { fill: none; stroke: var(--navy-dark); stroke-width: 1.6; stroke-linecap: round; stroke-linejoin: round; }
  .locations__title {
    font-family: "Barlow Semi Condensed", "Arial Narrow", sans-serif;
    font-weight: 600; font-size: 20px; letter-spacing: 0.5px;
  }
  .locations__list { font-size: 20px; line-height: 1.3; margin-top: 2px; }
  .sep { color: var(--orange); margin: 0 5px; }
</style>
</head>
<body>

  <section class="card card--info">
    <svg class="corners" viewBox="0 0 420 735" aria-hidden="true">
      <path d="M22 58 V22 H58"/><path d="M362 22 H398 V58"/>
      <path d="M22 677 V713 H58"/><path d="M362 713 H398 V677"/>
    </svg>
    <div class="brand">
      <div class="brand__name">LUMEN NORTH MEDIA</div>
      <div class="brand__tagline">Stories Told in Light</div>
    </div>
    <div class="details">
      <div class="person__name">MARISOL ORTEGA</div>
      <div class="person__role">FOUNDER &amp; MEDIA DIRECTOR</div>
      <div class="rule"></div>
      <ul class="contact">
        <li>
          <svg viewBox="0 0 26 26" aria-hidden="true"><circle class="icon-bg" cx="13" cy="13" r="13"/><path class="icon-line" d="M9 7.5c-1 1-1 3 1.5 6s5 4.5 6.5 3.5l1-1.2-2.2-1.8-1.2 1c-1-.5-2.6-2-3.2-3.3l1-1.2L10.6 7z"/></svg>
          <span>(305) 555-0148</span>
        </li>
        <li>
          <svg viewBox="0 0 26 26" aria-hidden="true"><circle class="icon-bg" cx="13" cy="13" r="13"/><rect class="icon-line" x="7" y="9" width="12" height="8.5"/><path class="icon-line" d="M7 9l6 5 6-5"/></svg>
          <span>marisol@lumennorthmedia.com</span>
        </li>
        <li>
          <svg viewBox="0 0 26 26" aria-hidden="true"><circle class="icon-bg" cx="13" cy="13" r="13"/><path class="icon-line" d="M13 20s-4.5-4.6-4.5-8a4.5 4.5 0 0 1 9 0c0 3.4-4.5 8-4.5 8z"/><circle class="icon-line" cx="13" cy="12" r="1.6"/></svg>
          <span>240 Harbor Lane, 4th Floor<br>Miami, FL 33130</span>
        </li>
      </ul>
      <div class="rule"></div>
      <div class="locations">
        <div class="locations__title">LOCATIONS</div>
        <div class="locations__list">Tampa<span class="sep">•</span>Boston<span class="sep">•</span>Denver<br>Austin<span class="sep">•</span>Lisboa</div>
      </div>
    </div>
  </section>

  <section class="card card--brand">
    <div class="pattern-area" role="img" aria-label="Subtle wavy line pattern in soft blue tones"></div>
    <svg class="corners" viewBox="0 0 420 735" aria-hidden="true">
      <path d="M22 58 V22 H58"/><path d="M362 22 H398 V58"/>
      <path d="M22 677 V713 H58"/><path d="M362 713 H398 V677"/>
    </svg>
    <div class="brand">
      <div class="brand__name">LUMEN NORTH MEDIA</div>
      <div class="brand__tagline">Stories Told in Light</div>
    </div>
  </section>

</body>
</html>
```